Harbor Ridge Capital and Investments

Create a simple business card design using the logos attached. Make it similar but not exact to the reference photo. Brand guidelines are also included.

```html
<!DOCTYPE html>
<html lang="en">
<head>
<meta charset="utf-8">
<title>Harbor Ridge Capital – Business Card</title>
<link rel="stylesheet" href="https://fonts.googleapis.com/css2?family=Arvo:wght@700&family=Poppins:wght@400&display=swap">
<style>
  :root {
    --navy: #000b3a;
    --navy-deep: #00072a;
    --blue-glow: #0a1f8a;
    --rust: #9a4713;
    --cream: #f3f0eb;
    --ink: #555555;
    --backdrop: #974513;
    --white: #ffffff;
  }
  * { margin: 0; padding: 0; box-sizing: border-box; }
  html, body {
    width: 1200px; height: 1200px; overflow: hidden;
    background: var(--backdrop);
  }
  .canvas { position: relative; width: 1200px; height: 1200px; }

  .card { position: absolute; width: 690px; height: 394px; overflow: hidden; }

  /* Front */
  .card-front { left: 266px; top: 158px; background: var(--cream); }
  .brand-name {
    position: absolute; left: 40px; top: 96px;
    font-family: "Arvo", serif; font-weight: 700;
    font-size: 27px; line-height: 1.18; letter-spacing: 2px;
    color: var(--navy); text-transform: uppercase;
  }
  .brand-mark {
    position: absolute; left: 40px; top: 40px;
    width: 40px; height: 40px; border-radius: 50%;
    background: var(--rust);
  }
  .address {
    position: absolute; left: 43px; top: 215px;
    font-family: "Poppins", sans-serif; font-size: 16px; line-height: 21px;
    color: var(--ink);
  }
  .contact-list {
    position: absolute; left: 43px; top: 270px; list-style: none;
    font-family: "Poppins", sans-serif; font-size: 16px; color: var(--ink);
  }
  .contact-list li { display: flex; align-items: center; height: 21px; }
  .contact-list svg { width: 14px; height: 14px; margin-right: 12px; fill: var(--navy); flex: none; }

  .person { position: absolute; right: 56px; top: 278px; text-align: right; }
  .person-name {
    font-family: "Arvo", serif; font-weight: 700; font-size: 25px;
    color: var(--navy); letter-spacing: 0.5px; line-height: 30px;
  }
  .person-title {
    font-family: "Poppins", sans-serif; font-size: 16px;
    color: var(--rust); line-height: 20px;
  }
  .accent-bar {
    position: absolute; right: 0; top: 279px; width: 27px; height: 48px;
    background: var(--navy);
  }

  /* Back */
  .card-back { left: 258px; top: 651px; background: var(--navy); }
  .pattern-field {
    position: absolute; inset: 0;
    background: linear-gradient(90deg, var(--navy-deep) 0%, var(--navy) 45%, rgba(10,31,138,0.55) 100%);
  }
  .back-name {
    position: absolute; left: 560px; top: 300px;
    font-family: "Arvo", serif; font-weight: 700; font-size: 13px;
    letter-spacing: 1px; color: var(--white); text-transform: uppercase;
  }
</style>
</head>
<body>
<main class="canvas">
  <section class="card card-front" aria-label="Business card front">
    <div class="brand-mark" aria-hidden="true"></div>
    <div class="brand-name">Harbor Ridge<br>Capital</div>

    <p class="address">214 Lantern Bay Road<br>Seabrook, Canada 48102</p>

    <ul class="contact-list">
      <li>
        <svg viewBox="0 0 24 24" aria-hidden="true"><path d="M6.6 10.8a15.1 15.1 0 0 0 6.6 6.6l2.2-2.2c.3-.3.7-.4 1-.2 1.1.4 2.3.6 3.6.6.6 0 1 .4 1 1V20c0 .6-.4 1-1 1A17 17 0 0 1 3 4c0-.6.4-1 1-1h3.5c.6 0 1 .4 1 1 0 1.3.2 2.5.6 3.6.1.3 0 .7-.2 1z"/></svg>
        512-380-1947
      </li>
      <li>
        <svg viewBox="0 0 24 24" aria-hidden="true"><path d="M7 1h10a2 2 0 0 1 2 2v18a2 2 0 0 1-2 2H7a2 2 0 0 1-2-2V3a2 2 0 0 1 2-2zm0 3v15h10V4zm4 16.2h2v1.3h-2z"/></svg>
        512-906-2281
      </li>
      <li>
        <svg viewBox="0 0 24 24" aria-hidden="true"><path d="M2 5h20v14H2zm2 2v.4l8 5.2 8-5.2V7zm0 2.8V17h16V9.8l-8 5.2z"/></svg>
        hello@harborridgecap.com
      </li>
      <li>
        <svg viewBox="0 0 24 24" aria-hidden="true"><path d="M12 2a10 10 0 1 0 0 20 10 10 0 0 0 0-20zm-1 17.9A8 8 0 0 1 4.2 10L9 14.8v1c0 1.1.9 2 2 2zm6.9-2.5A2 2 0 0 0 16 16h-1v-3a1 1 0 0 0-1-1H8v-2h2a1 1 0 0 0 1-1V7h2a2 2 0 0 0 2-2v-.4a8 8 0 0 1 2.9 12.8z"/></svg>
        www.harborridgecap.com
      </li>
    </ul>

    <div class="person">
      <div class="person-name">DANIEL REYES</div>
      <div class="person-title">President</div>
    </div>
    <div class="accent-bar" aria-hidden="true"></div>
  </section>

  <section class="card card-back" aria-label="Business card back">
    <div class="pattern-field" role="img" aria-label="Repeating brand pattern in deep navy fading to blue"></div>
    <div class="back-name">Harbor Ridge</div>
  </section>
</main>
</body>
</html>
```